Riverbend Strong Unions and Households Project-Postcard

We need a postcard to promote our program. We will use the postcard to remind clients of appointments or even use it as a marketing tool when we go out to events. We provide healthy relationship education, financial classes and job readiness education. Our target population is adult couples. Mostly Spanish speaking. If its possible to incorporate all three components into the design that would be great, if not, healthy relationship would be our priority.

Attached is a logo we would like to use.

I have also included the text we would like to use. Would you please make all text editable incase we want to add different text.

The funding statement has to go at the bottom (it can be in small text).

Industry/Entity Type

Marketing

Requirements
Must have
• if you use images of people, please use Latino images. Our target population is Spanish speaking.

```html
<!DOCTYPE html>
<html lang="es">
<head>
<meta charset="utf-8">
<title>Riverbend Strong Unions and Households Project – Postcard</title>
<link rel="stylesheet" href="https://fonts.googleapis.com/css2?family=Ubuntu:wght@300;500;700&family=Oswald:wght@500;600&family=Open+Sans:wght@400;600;700&display=swap">
<style>
  :root{
    --page:#e6e6e8;
    --card:#ffffff;
    --navy:#1b4f86;
    --navy-deep:#17467a;
    --magenta:#c8155a;
    --red:#d81f34;
    --orange:#e0862b;
    --ink:#222222;
    --mist-a:#f1f1f2;
    --mist-b:#d9d9db;
    --photo-blue-a:#2c5f86;
    --photo-blue-b:#143f68;
  }
  *{box-sizing:border-box;margin:0;padding:0}
  html,body{width:766px;height:1200px;overflow:hidden}
  body{background:var(--page);position:relative;font-family:"Open Sans",sans-serif}

  .postcard{position:absolute;left:45px;width:675px;height:520px;background:var(--card);overflow:hidden}
  .postcard--front{top:45px}
  .postcard--back{top:635px;height:518px}

  /* front */
  .front-backdrop{position:absolute;inset:0;background:linear-gradient(135deg,var(--mist-a),var(--mist-b))}
  .brand{position:absolute;display:flex;align-items:center;gap:8px;font-family:"Ubuntu",sans-serif;font-weight:700;color:var(--navy);line-height:1.1}
  .brand__dot{width:22px;height:22px;border-radius:50%;background:var(--magenta);flex:none}
  .postcard--front .brand{left:50px;top:52px;font-size:22px;width:230px}

  .couple-photo{position:absolute;left:290px;top:14px;width:372px;height:494px;border-radius:48px;
    background:radial-gradient(circle at 45% 40%,#e2354f 0%,var(--red) 45%,#a3122a 100%)}

  .band{position:absolute;left:0}
  .band--headline{top:157px;width:300px;height:145px;background:var(--navy)}
  .band--info{top:302px;width:300px;height:52px;background:var(--navy-deep)}
  .band--phone{top:354px;width:300px;height:46px;background:var(--magenta)}

  .headline{position:absolute;left:48px;top:160px;color:#fff;font-family:"Ubuntu",sans-serif;line-height:1}
  .headline__lead{display:block;font-weight:700;font-size:37px;margin-bottom:4px}
  .headline__line{display:block;font-weight:500;font-size:24px;margin-bottom:3px}
  .headline__line--light{font-weight:300;font-size:22px}
  .headline__line--strong{font-weight:700;font-size:30px}

  .call{position:absolute;left:48px;top:310px;color:#fff;font-family:"Oswald",sans-serif;font-weight:500;line-height:1}
  .call__small{display:block;font-size:16px;padding-left:16px}
  .call__big{display:block;font-size:21px;margin-top:2px}
  .phone{position:absolute;left:48px;top:357px;color:#fff;font-family:"Oswald",sans-serif;font-weight:600;font-size:32px;line-height:1.2}

  .program{position:absolute;left:50px;top:428px;width:240px;display:flex;align-items:center;gap:8px;
    font-family:"Ubuntu",sans-serif;font-weight:500;font-size:15px;line-height:1.2;color:var(--orange)}
  .program__dot{width:16px;height:16px;border-radius:50%;background:var(--orange);flex:none}

  /* back */
  .back-art{position:absolute;left:0;top:0}
  .funding{position:absolute;left:43px;top:46px;width:245px;color:#fff;font-size:14.5px;line-height:21px}
  .funding strong{font-weight:600}
  .back-call{position:absolute;left:0;top:298px;width:285px;height:76px;background:var(--magenta);color:#fff;padding:10px 0 0 42px}
  .back-call__label{font-size:12px;line-height:1}
  .back-call__label strong{font-weight:700}
  .back-call__phone{font-family:"Oswald",sans-serif;font-weight:600;font-size:32px;line-height:1.25}
  .postcard--back .brand{left:378px;top:72px;font-size:17px;width:160px}
  .postcard--back .brand__dot{width:18px;height:18px}
  .stamp-box{position:absolute;left:533px;top:41px;width:98px;height:99px;border:1.5px solid var(--ink)}
  .address-line{position:absolute;left:400px;width:231px;height:0;border-top:1px solid var(--ink)}
  .address-line--1{top:253px}
  .address-line--2{top:298px}
  .address-line--3{top:343px}
</style>
</head>
<body>

<section class="postcard postcard--front">
  <div class="front-backdrop" role="img" aria-label="Soft grey photo of autumn leaves and a knit blanket"></div>
  <div class="brand"><span class="brand__dot"></span>Riverbend Community Partners</div>

  <div class="band band--headline"></div>
  <div class="band band--info"></div>
  <div class="band band--phone"></div>

  <div class="couple-photo" role="img" aria-label="Red-toned photo of a smiling Latino couple embracing"></div>

  <h1 class="headline">
    <span class="headline__lead">...porque</span>
    <span class="headline__line">una relación</span>
    <span class="headline__line headline__line--light">sana está a</span>
    <span class="headline__line headline__line--strong">su alcance</span>
  </h1>
  <p class="call"><span class="call__small">Para más información</span><span class="call__big">llame a</span></p>
  <p class="phone">555-201-4870</p>

  <div class="program"><span class="program__dot"></span>Riverbend Strong Unions and Households Project</div>
</section>

<section class="postcard postcard--back">
  <svg class="back-art" width="675" height="518" viewBox="0 0 675 518">
    <defs>
      <linearGradient id="familyTone" x1="0" y1="0" x2="1" y2="1">
        <stop offset="0" stop-color="var(--photo-blue-a)"/>
        <stop offset="1" stop-color="var(--photo-blue-b)"/>
      </linearGradient>
    </defs>
    <path role="img" aria-label="Blue-toned photo of a Latino family outdoors"
      d="M0 0 L255 0 C340 70 372 170 335 280 C308 360 272 410 238 445 L0 445 Z" fill="url(#familyTone)"/>
    <path d="M262 0 L284 0 C398 72 424 192 386 300 C356 382 312 422 284 445 L270 445 C298 410 338 360 360 290 C390 190 366 80 262 0 Z" fill="var(--magenta)"/>
  </svg>

  <p class="funding">Funding for this project was provided by the <strong>National Department of Family Services,</strong> Office for Children and Households, Grant: #47RB2291. These services are available to all eligible persons, regardless of race, gender, age, disability, or religion.</p>

  <div class="back-call">
    <p class="back-call__label">Para <strong>más información llame a</strong></p>
    <p class="back-call__phone">555-201-4870</p>
  </div>

  <div class="brand"><span class="brand__dot"></span>Riverbend Community Partners</div>
  <div class="stamp-box"></div>
  <div class="address-line address-line--1"></div>
  <div class="address-line address-line--2"></div>
  <div class="address-line address-line--3"></div>
</section>

</body>
</html>
```